Marcus Tellow album cover "Borrowed Lanterns, Quiet Harbors"

3000x3000 album cover using attached image and provided text needed for cover of upcoming album for Seattle musician. Only front cover needed at this time.

Font styles to use
Serif
Sans Serif

Colors

Designer to choose colors to be used in the design.

```html
<!DOCTYPE html>
<html lang="en">
<head>
<meta charset="utf-8">
<title>Marcus Tellow – Borrowed Lanterns, Quiet Harbors</title>
<link rel="stylesheet" href="https://fonts.googleapis.com/css2?family=Cormorant+Garamond:wght@500&family=Questrial&display=swap">
<style>
  :root {
    --cover-paper: #ffffff;
    --ink: #111111;
    --night-sky: #1a2230;
    --night-foliage: #26331f;
    --roof-dusk: #3a3430;
    --lit-wall: #9a8a78;
    --lamp-glow: #e2b878;
    --trailer-light: #f4f1ea;
    --copper-glow: #d99a3c;
    --lawn-shadow: #4f6a2c;
    --lawn-lit: #8fb446;
  }
  * { margin: 0; padding: 0; box-sizing: border-box; }
  html, body {
    width: 1200px;
    height: 1200px;
    overflow: hidden;
    background: var(--cover-paper);
  }
  .album-cover {
    position: relative;
    width: 1200px;
    height: 1200px;
    background: var(--cover-paper);
    color: var(--ink);
  }
  .album-title {
    position: absolute;
    top: 36px;
    left: 0;
    width: 100%;
    text-align: center;
    font-family: "Questrial", "Century Gothic", sans-serif;
    font-weight: 400;
    font-size: 84px;
    line-height: 85px;
    letter-spacing: 0.5px;
  }
  .album-title .title-line { display: block; }
  .photo-strips {
    position: absolute;
    top: 0;
    left: 0;
    width: 1200px;
    height: 1200px;
  }
  .artist-name {
    position: absolute;
    top: 1124px;
    left: 0;
    width: 100%;
    text-align: center;
    font-family: "Cormorant Garamond", "Garamond", serif;
    font-weight: 500;
    font-size: 52px;
    line-height: 52px;
    letter-spacing: 1px;
  }
</style>
</head>
<body>
  <main class="album-cover">
    <h1 class="album-title">
      <span class="title-line">Borrowed Lanterns</span>
      <span class="title-line">Quiet Harbors</span>
    </h1>

    <svg class="photo-strips" viewBox="0 0 1200 1200" xmlns="http://www.w3.org/2000/svg"
         role="img" aria-label="Night photograph of vintage camper trailers lit up on a grassy yard among trees, cut into six vertical strips">
      <defs>
        <linearGradient id="night-yard" gradientUnits="userSpaceOnUse" x1="0" y1="230" x2="0" y2="1110">
          <stop offset="0" stop-color="var(--night-sky)"/>
          <stop offset="0.22" stop-color="var(--night-foliage)"/>
          <stop offset="0.36" stop-color="var(--roof-dusk)"/>
          <stop offset="0.5" stop-color="var(--lit-wall)"/>
          <stop offset="0.66" stop-color="var(--lawn-shadow)"/>
          <stop offset="1" stop-color="var(--lawn-lit)"/>
        </linearGradient>
        <radialGradient id="camper-glow" gradientUnits="userSpaceOnUse" cx="610" cy="640" r="330">
          <stop offset="0" stop-color="var(--trailer-light)" stop-opacity="0.85"/>
          <stop offset="0.5" stop-color="var(--lamp-glow)" stop-opacity="0.35"/>
          <stop offset="1" stop-color="var(--lamp-glow)" stop-opacity="0"/>
        </radialGradient>
        <radialGradient id="copper-trailer-glow" gradientUnits="userSpaceOnUse" cx="1130" cy="600" r="220">
          <stop offset="0" stop-color="var(--copper-glow)" stop-opacity="0.9"/>
          <stop offset="1" stop-color="var(--copper-glow)" stop-opacity="0"/>
        </radialGradient>
        <radialGradient id="window-glow" gradientUnits="userSpaceOnUse" cx="180" cy="620" r="230">
          <stop offset="0" stop-color="var(--lamp-glow)" stop-opacity="0.55"/>
          <stop offset="1" stop-color="var(--lamp-glow)" stop-opacity="0"/>
        </radialGradient>
        <clipPath id="strip-cuts">
          <rect x="0"   y="271" width="173" height="755"/>
          <rect x="185" y="320" width="192" height="789"/>
          <rect x="388" y="231" width="172" height="753"/>
          <rect x="576" y="288" width="217" height="759"/>
          <rect x="807" y="323" width="168" height="585"/>
          <rect x="987" y="323" width="213" height="756"/>
        </clipPath>
      </defs>
      <g class="strip-set" clip-path="url(#strip-cuts)">
        <rect class="scene-base" x="0" y="220" width="1200" height="900" fill="url(#night-yard)"/>
        <rect class="scene-window-light" x="0" y="220" width="1200" height="900" fill="url(#window-glow)"/>
        <rect class="scene-camper-light" x="0" y="220" width="1200" height="900" fill="url(#camper-glow)"/>
        <rect class="scene-copper-light" x="0" y="220" width="1200" height="900" fill="url(#copper-trailer-glow)"/>
      </g>
    </svg>

    <p class="artist-name">Marcus Tellow</p>
  </main>
</body>
</html>
```